Harbor Key Realty - New Agent Opportunity Overview

We want to create a one (1) page brochure to highlight what Harbor Key Realty (a real estate brokerage) offers new agents. I have uploaded a Word doc that has all the text we want on the flyer. We want a professional looking design.
Industry/Entity Type
Real Estate Agent
Colors
3176b5
33a6d7

```html
<!DOCTYPE html>
<html lang="en">
<head>
<meta charset="utf-8">
<title>Harbor Key Realty – New Agent Opportunity</title>
<link rel="stylesheet" href="https://fonts.googleapis.com/css2?family=Montserrat:ital,wght@1,800&family=Roboto:wght@400;500;700&display=swap">
<style>
:root{
  --stage:#3a3a3c;
  --paper:#ffffff;
  --ink:#111111;
  --violet:#5558e6;
  --violet-deep:#4346c9;
  --sky:#2fa3de;
  --panel:#000000;
  --white:#ffffff;
}
*{margin:0;padding:0;box-sizing:border-box}
html,body{width:1200px;height:1200px;overflow:hidden;background:var(--stage);font-family:'Roboto',sans-serif}
.flyer{position:absolute;left:188px;top:53px;width:839px;height:1085px;background:var(--paper);overflow:hidden}
.flyer > *,.comp-row > *{position:absolute}
.brand{left:67px;top:38px;font:700 30px/1 'Roboto',sans-serif;letter-spacing:4px;color:var(--ink);white-space:nowrap}
.hero-photo{left:0;top:117px;width:839px;height:240px;background:linear-gradient(180deg,#5a9be0 0%,#b9d3ea 45%,#7fa870 70%,#4f8a2e 100%);z-index:0}
.ribbon{left:518px;top:22px;width:321px;height:192px;z-index:2}
.ribbon-title{left:518px;top:55px;width:266px;text-align:center;color:var(--white);font:500 23px/1 'Roboto',sans-serif;z-index:2}
.ribbon-place{left:518px;top:82px;width:266px;text-align:center;color:var(--white);font:500 19px/1 'Roboto',sans-serif;z-index:2}
.ribbon-open{left:535px;top:117px;width:233px;height:50px;background:var(--panel);border:2px solid var(--white);color:var(--white);font:700 31px/46px 'Roboto',sans-serif;text-align:center;z-index:2}
.kicker{left:0;top:374px;width:839px;text-align:center;color:var(--violet);font:500 26px/1 'Roboto',sans-serif}
.headline{left:0;top:408px;width:839px;text-align:center;color:var(--ink);font:800 italic 49px/1.1 'Montserrat',sans-serif;white-space:nowrap}
.headline em{font-style:italic;color:var(--violet)}
.offer{left:0;top:475px;width:839px;height:610px;background:linear-gradient(180deg,var(--violet) 0%,#4a79ea 45%,var(--sky) 100%)}
.offer-shadow{left:0;top:475px;width:839px;height:8px;background:linear-gradient(180deg,rgba(0,0,0,.25),transparent)}
.skyline{left:380px;top:910px;width:459px;height:120px;background:linear-gradient(180deg,rgba(80,110,240,0),rgba(60,70,220,.9))}
.advantage-panel{left:44px;top:504px;width:331px;height:500px;background:var(--panel)}
.tag{background:var(--violet);color:var(--white);font:500 19px/36px 'Roboto',sans-serif;padding-left:7px;white-space:nowrap}
.tag-direct{left:58px;top:519px;width:303px}
.tag-comp{left:58px;top:756px;width:303px;font-size:20px;padding-left:12px}
.ticks{list-style:none}
.ticks li{position:relative;padding-left:25px;color:var(--white);font:400 16px/19.2px 'Roboto',sans-serif;white-space:nowrap}
.ticks li::before{content:"✓";position:absolute;left:3px;top:0;color:#9fa2ff;font-size:14px}
.ticks-direct{left:70px;top:566px;width:300px}
.comp-row{left:62px;width:300px;height:40px}
.comp-icon{left:0;top:0;width:36px;height:36px;border-radius:50%;background:var(--violet);color:var(--white);font:700 13px/36px 'Roboto',sans-serif;text-align:center}
.comp-text{left:48px;top:0;color:var(--white);font:400 16px/19.2px 'Roboto',sans-serif;width:260px;white-space:nowrap}
.comp-text b{font-weight:700}
.split-frame{left:400px;top:540px;width:413px;height:113px}
.split-title{left:470px;top:505px;width:270px;color:var(--white);font:500 24px/25px 'Roboto',sans-serif;text-align:center}
.split-row{left:413px;color:var(--white);font:400 15px/22px 'Roboto',sans-serif;white-space:nowrap}
.split-row b{font:500 20px/22px 'Roboto',sans-serif;margin-left:4px}
.split-row b.far{margin-left:12px}
.tag-support{left:445px;top:683px;width:313px;height:36px;background:var(--panel);color:var(--white);font:500 20px/36px 'Roboto',sans-serif;text-align:center}
.ticks-support{left:443px;top:727px;width:390px}
.ticks-support li{font-size:16.5px}
.ticks-support li::before{color:var(--ink)}
.footer-wave{left:0;top:955px;width:839px;height:130px}
.contact{left:65px;top:987px;color:var(--ink);font:500 16px/19.5px 'Roboto',sans-serif}
.web{left:65px;top:1046px;color:var(--violet-deep);font:700 22px/1 'Roboto',sans-serif}
.social{left:590px;top:1055px;width:130px;height:20px}
</style>
</head>
<body>
<main class="flyer">
  <div class="hero-photo" role="img" aria-label="Photo of a large white two-storey family home with a green lawn under a blue sky"></div>
  <div class="brand">HARBOR KEY REALTY</div>

  <svg class="ribbon" viewBox="0 0 321 192" aria-hidden="true">
    <path d="M270 0 H300 Q321 0 321 30 V95 H270 Z" fill="#4346c9"/>
    <path d="M30 0 H290 Q266 0 266 30 V165 L133 192 L0 165 V30 Q0 0 30 0 Z" fill="#5558e6"/>
  </svg>
  <div class="ribbon-title">HKR HOME CENTER</div>
  <div class="ribbon-place">Gaithersburg, Maryland</div>
  <div class="ribbon-open">IS NOW OPEN!</div>

  <div class="kicker">IGNITE YOUR REAL ESTATE BUSINESS</div>
  <div class="headline"><em>Join</em> Harbor Key Realty!</div>

  <section class="offer"></section>
  <div class="offer-shadow"></div>
  <div class="skyline" role="img" aria-label="Illustration of a blue city skyline"></div>

  <div class="advantage-panel"></div>
  <div class="tag tag-direct">CONSUMER DIRECT ADVANTAGE</div>
  <ul class="ticks ticks-direct">
    <li>Lender Referrals</li>
    <li>Homefindr Leads</li>
    <li>Shared Lender Leads</li>
    <li>Listingsphere.com /<br>NearbyHomeFinder.com</li>
    <li>Credit Trigger Campaigns</li>
    <li>Consumer Behavior Campaigns</li>
    <li>HKR Call Center Marketing Team</li>
    <li>HKR Sponsored Local Events</li>
  </ul>

  <div class="tag tag-comp">MAXIMIZED COMPENSATION</div>
  <div class="comp-row" style="top:812px">
    <div class="comp-icon">%</div>
    <div class="comp-text"><b>NO</b> desk fees. <b>NO</b> royalty fees.<br><b>NO</b> franchise fees.</div>
  </div>
  <div class="comp-row" style="top:860px">
    <div class="comp-icon">$</div>
    <div class="comp-text" style="top:9px">Company paid E&amp;O</div>
  </div>
  <div class="comp-row" style="top:908px">
    <div class="comp-icon">$550</div>
    <div class="comp-text">Transaction fee of $550<br>includes Transaction Coordinator</div>
  </div>

  <svg class="split-frame" viewBox="0 0 413 113" aria-hidden="true">
    <path d="M70 1.5 H1.5 V111.5 H411.5 V1.5 H332" fill="none" stroke="#ffffff" stroke-width="3"/>
  </svg>
  <div class="split-title">TYPE OF DEAL<br>COMMISSION SPLIT</div>
  <div class="split-row" style="top:567px">SELF-GENERATED<b>90% / 10%</b></div>
  <div class="split-row" style="top:591px">LENDER REFERRED LEADS<b>70% / 30%</b></div>
  <div class="split-row" style="top:615px">HKR GENERATED LEADS / REFERRALS<b class="far">55% / 45%</b></div>

  <div class="tag-support">COMPLETE SUPPORT SYSTEM</div>
  <ul class="ticks ticks-support">
    <li>Powerful Suite of Cloud Based Tools</li>
    <li>IDX, CRM and Transaction Management</li>
    <li>HKR Call Center Support for Leads and Deals</li>
    <li>Transaction Coordinator</li>
    <li>Virtual Assistants Available</li>
    <li>24/7 Workspace Access</li>
    <li>Coaching / Mentoring</li>
    <li>Social Media / Marketing Expertise</li>
    <li>Nationwide Partnerships with Top Lenders</li>
  </ul>

  <svg class="footer-wave" viewBox="0 0 839 130" aria-hidden="true">
    <path d="M0 18 Q210 -8 420 40 Q640 92 839 65 V130 H0 Z" fill="#ffffff"/>
    <path d="M0 18 Q210 -8 420 40 Q640 92 839 65" fill="none" stroke="#5558e6" stroke-width="5"/>
  </svg>
  <div class="contact">Address<br>Phone<br>Email</div>
  <div class="web">www.website.com</div>
  <svg class="social" viewBox="0 0 130 20" aria-hidden="true">
    <circle cx="10" cy="10" r="9" fill="#4346c9"/>
    <circle cx="36" cy="10" r="9" fill="#4346c9"/>
    <circle cx="62" cy="10" r="9" fill="#4346c9"/>
    <circle cx="88" cy="10" r="9" fill="#4346c9"/>
    <circle cx="114" cy="10" r="9" fill="#4346c9"/>
  </svg>
</main>
</body>
</html>
```